Buchcover-Design für Finanz-Ratgeber zum Thema Börse
Zielgruppe
Es handelt sich um einen Finanz-Ratgeber zum Thema Börse (allgemein), Geldanlage (allgemein) und ETFs (im Speziellen).
Zielgruppe: Männer, 20-35.
Das Buch ist an Anfänger und Privatanleger ausgerichtet.
Es handelt sich um einen populär-Ratgeber und NICHT um ein wissenschaftliches Buch.
Aufgabenstellung
Das Cover sollte finanziellen Erfolg und Reichtum an der Börse ausstrahlen. Es soll NICHT wie ein wissenschaftliches Buch aussehen, sondern lebendiger und aufregender.
Bitte in Farbgestaltung und Hintergrundbild am Beispielbild orientieren. Farbgestaltung hauptsächlich gold-farben und NICHT Schwarz-lastig, wie es die Konkurrenz für ETF-Bücher tut.
Als Elemente sollen im Hintergrund Aktiencharts in Form von 'Candlesticks Charts' (siehe Beispielbild, im Zweifel einfach googlen) verwendet werden. Der Hintergrund sollte nicht einfarbig sein, sondern transparente Elemente aufweisen. Bitte ziehen Sie diese Elemente, Muster oder Texturen auch über Buchrücken und Rückseite.
Falls Sie Stockmaterial verwenden, nutzen Sie bitte Bildkontor.
Titel: Der Fonds-Kompass
Subtitel: Wie Sie in ETFs investieren und die besten ETFs für Ihr Portfolio finden
Autoren-Name: Markus Welder
Verlags-Logo unten links (farblich anpassen)
Format: 6x9 Zoll, 210 Seiten (bitte Template benutzen)
Das Endergebnis wird ebenfalls als .svg-Datei benötigt.
Rückseite:
Bitte verwenden Sie das Autorenbild im Anhang. Setzen Sie es eingerückt zu Beginn der Autoren-Beschreibung, in Kreisform, ca. 1,5x1,5 cm groß.
Bitte bauen Sie unten links auf der Rückseite, neben dem ISBN-Code ein Internet-Symbol sowie folgenden Link ein:
https://geldwege-beispiel.de
Klappentext (in Blocksatz)
Wollen Sie endlich den Schritt wagen und in ETFs investieren, aber bei der großen Auswahl an verfügbaren Anlageprodukten wissen Sie einfach nicht, welche(n) Sie auswählen sollen? Sie sind unsicher, auf welche Kriterien Sie achten müssen, um die kostengünstigsten und vertrauenswürdigsten ETFs für Ihr Depot zu finden? Sie haben die Begriffe „synthetisch“ oder „thesaurierend“ zwar schon einmal gehört, wissen aber nicht, wie gut oder schlecht solche ETFs zu Ihnen passen?
Dann wird Ihnen Der Fonds-Kompass alle Fragen beantworten können..

```html
<!DOCTYPE html>
<html lang="de">
<head>
<meta charset="utf-8">
<title>Der Fonds-Kompass – Umschlag</title>
<link rel="stylesheet" href="https://fonts.googleapis.com/css2?family=Raleway:wght@400;500;600;700;800&display=swap">
<style>
  :root {
    --page-bg: #ffffff;
    --gold: #c9b548;
    --gold-light: #e4d675;
    --gold-dark: #a8962f;
    --olive: #857731;
    --olive-text: #6d6532;
    --band: rgba(160, 140, 40, 0.45);
    --glow: #fff24a;
    --white: #ffffff;
  }
  * { margin: 0; padding: 0; box-sizing: border-box; }
  html, body { width: 960px; height: 1200px; overflow: hidden; background: var(--page-bg); }
  .canvas { position: relative; width: 960px; height: 1200px; }
  .cover-spread {
    position: absolute; left: 30px; top: 275px;
    width: 1240px; height: 895px;
    transform: scale(0.7258); transform-origin: 0 0;
    background: linear-gradient(160deg, var(--gold-light) 0%, var(--gold) 45%, var(--gold-dark) 100%);
    overflow: hidden;
    font-family: 'Raleway', sans-serif;
    box-shadow: 0 2px 6px rgba(0,0,0,0.25);
  }
  .chart-layer { position: absolute; inset: 0; }

  /* back cover */
  .blurb {
    position: absolute; left: 105px; top: 82px; width: 387px;
    color: var(--white); font-size: 12.4px; line-height: 16.6px;
    font-weight: 500; text-align: justify; hyphens: auto;
  }
  .blurb p + p { margin-top: 16px; }
  .author-bio {
    position: absolute; left: 105px; top: 430px; width: 387px;
    color: var(--white); font-size: 12.4px; line-height: 16.6px;
    font-weight: 500; text-align: justify;
  }
  .author-portrait {
    float: left; width: 60px; height: 60px; border-radius: 50%;
    margin: 3px 6px 2px 0;
    background: radial-gradient(circle at 50% 40%, #d8d2c0, #8d866e);
    border: 2px solid rgba(255,255,255,0.6);
  }
  .author-name-caps { color: var(--olive-text); }
  .info-band {
    position: absolute; left: 0; top: 750px; width: 355px; height: 117px;
    background: var(--band);
  }
  .web-link {
    position: absolute; left: 92px; top: 825px;
    display: flex; align-items: center; gap: 8px;
    color: var(--white); font-size: 13.5px; font-weight: 600;
  }
  .isbn-box {
    position: absolute; left: 373px; top: 750px; width: 198px; height: 117px;
    background: var(--white);
  }

  /* spine */
  .spine-text {
    position: absolute; color: var(--olive-text); font-size: 14px; font-weight: 500;
    transform: rotate(-90deg); transform-origin: 0 0; white-space: nowrap;
  }
  .spine-author { left: 613px; top: 528px; }
  .spine-title { left: 613px; top: 668px; }
  .spine-publisher { left: 613px; top: 865px; }

  /* front cover */
  .front-author {
    position: absolute; left: 965px; top: 82px;
    color: var(--olive-text); font-size: 27px; font-weight: 500;
  }
  .front-title {
    position: absolute; left: 690px; top: 195px; width: 540px;
    color: var(--olive); opacity: 0.85; font-weight: 800; text-transform: uppercase;
  }
  .title-der { display: block; font-size: 66px; line-height: 66px; font-weight: 700; margin-left: 150px; letter-spacing: -2px; }
  .title-main { display: block; font-size: 104px; line-height: 104px; letter-spacing: -4px; }
  .subtitle-band {
    position: absolute; left: 790px; top: 535px; width: 450px; height: 80px;
    background: var(--band);
  }
  .subtitle {
    position: absolute; left: 808px; top: 546px; width: 420px;
    color: var(--white); font-size: 21px; line-height: 27px; font-weight: 500;
  }
  .publisher-mark {
    position: absolute; left: 692px; top: 800px;
    color: var(--olive-text); font-size: 28px; font-weight: 600; letter-spacing: 1px;
  }
</style>
</head>
<body>
<div class="canvas">
  <div class="cover-spread">
    <svg class="chart-layer" viewBox="0 0 1240 895" aria-hidden="true">
      <defs>
        <radialGradient id="glowSpot" cx="0.78" cy="0.78" r="0.35">
          <stop offset="0" stop-color="#fff46a" stop-opacity="0.55"/>
          <stop offset="1" stop-color="#fff46a" stop-opacity="0"/>
        </radialGradient>
      </defs>
      <rect width="1240" height="895" fill="url(#glowSpot)"/>
      <g stroke="#ffffff" stroke-opacity="0.08">
        <path d="M0 120H1240M0 240H1240M0 360H1240M0 480H1240M0 600H1240M0 720H1240M0 840H1240"/>
        <path d="M140 0V895M300 0V895M460 0V895M780 0V895M940 0V895M1100 0V895"/>
      </g>
      <g class="candles" fill="#f3ea9c" fill-opacity="0.45">
        <rect x="30" y="330" width="12" height="70"/><rect x="70" y="300" width="12" height="60"/>
        <rect x="110" y="240" width="12" height="90"/><rect x="150" y="270" width="12" height="40"/>
        <rect x="190" y="215" width="12" height="70"/><rect x="230" y="190" width="12" height="45"/>
        <rect x="400" y="380" width="12" height="60"/><rect x="440" y="330" width="12" height="70"/>
        <rect x="480" y="420" width="12" height="50"/>
        <rect x="690" y="200" width="14" height="30"/><rect x="740" y="220" width="14" height="40"/>
        <rect x="800" y="230" width="14" height="50"/><rect x="860" y="210" width="14" height="40"/>
        <rect x="1020" y="170" width="14" height="70"/><rect x="1060" y="200" width="14" height="50"/>
        <rect x="1120" y="165" width="14" height="30"/><rect x="1145" y="140" width="14" height="40"/>
        <rect x="1170" y="120" width="14" height="70"/><rect x="1200" y="90" width="14" height="60"/>
        <rect x="1225" y="40" width="12" height="70"/>
      </g>
      <g stroke="#f3ea9c" stroke-opacity="0.4" stroke-width="2">
        <path d="M36 310V420M116 220V350M196 200V300M446 310V420M746 200V280M1066 180V270M1176 100V210M1206 70V170"/>
      </g>
      <polyline fill="none" stroke="#f6ef9a" stroke-opacity="0.35" stroke-width="2"
        points="0,700 60,680 120,730 180,660 240,710 300,640 360,700 420,600 480,660 540,560 600,690 640,620"/>
      <polyline fill="none" stroke="var(--glow)" stroke-width="3" stroke-opacity="0.9"
        points="640,880 690,820 730,780 770,830 820,760 860,700 900,780 950,690 990,730 1030,680 1080,720 1130,640 1180,680 1240,620"/>
      <polyline fill="none" stroke="var(--glow)" stroke-width="8" stroke-opacity="0.25"
        points="640,880 690,820 730,780 770,830 820,760 860,700 900,780 950,690 990,730 1030,680 1080,720 1130,640 1180,680 1240,620"/>
      <g fill="#ffffff" fill-opacity="0.3" font-family="Raleway, sans-serif" font-size="22">
        <text x="2" y="540">Nov</text><text x="545" y="530">Jan</text>
        <text x="790" y="525">Feb</text><text x="1010" y="525">Mar</text><text x="1190" y="508">Apr</text>
      </g>
    </svg>

    <div class="blurb">
      <p>Wollen Sie endlich den Schritt wagen und in ETFs investieren, aber bei der großen Auswahl an verfügbaren Anlageprodukten wissen Sie einfach nicht, welche(n) Sie auswählen sollen? Sie sind unsicher, auf welche Kriterien Sie achten müssen, um die kostengünstigsten und vertrauenswürdigsten ETFs für Ihr Depot zu finden? Sie haben die Begriffe „synthetisch“ oder „thesaurierend“ zwar schon einmal gehört, wissen aber nicht, wie gut oder schlecht solche ETFs zu Ihnen passen?</p>
      <p>Dann wird Ihnen der Fonds-Kompass alle Fragen beantworten können – und noch viele mehr. Der Fonds-Kompass erklärt Ihnen in verständlicher Sprache, worauf es bei der Auswahl des richtigen ETFs ankommt und worauf man bei der Zusammenstellung seines ETF-Portfolios achten sollte. In einfachen Worten werden Ihnen die wichtigsten Fachbegriffe erklärt, die Sie zur Zusammenstellung ihres ETFs-Portfolios benötigen und die sich positiv auf den Erfolg ihrer Geldanlage auswirken werden.</p>
    </div>

    <div class="author-bio">
      <div class="author-portrait" role="img" aria-label="Rundes Porträtfoto des Autors"></div>
      <p><span class="author-name-caps">MARKUS WELDER</span> ist neben seiner Tätigkeit als Buchautor seit 2015 als freiberuflicher Autor für die Finanz-Homepage anlegerwelt.de tätig und hat dort inzwischen über 500 Artikel rund um Aktien, Börse und Co. verfasst.<br>Seit rund zwei Jahren betreibt er außerdem einen eigenen Blog, in dem er von seinen Käufen, Verkäufen, Dividenden und neuen Anlageideen berichtet. Von Aktien über ETFs bis hin zu Crowdinvestings teilt er in seinem Blog all seine Erfahrungen mit seinen Lesern.</p>
    </div>

    <div class="info-band"></div>
    <div class="web-link">
      <svg width="22" height="22" viewBox="0 0 22 22" aria-hidden="true" fill="none" stroke="var(--olive-text)" stroke-width="1.4">
        <circle cx="11" cy="11" r="9.5"/><ellipse cx="11" cy="11" rx="4" ry="9.5"/>
        <path d="M1.5 11H20.5M3 6H19M3 16H19"/>
      </svg>
      <span>https://geldwege-beispiel.de</span>
    </div>
    <div class="isbn-box"></div>

    <span class="spine-text spine-author">Markus Welder</span>
    <span class="spine-text spine-title">Der Fonds-Kompass</span>
    <span class="spine-text spine-publisher">kvm Verlag</span>

    <div class="front-author">Markus Welder</div>
    <h1 class="front-title">
      <span class="title-der">Der</span>
      <span class="title-main">Fonds-</span>
      <span class="title-main">Kompass</span>
    </h1>
    <div class="subtitle-band"></div>
    <p class="subtitle">Wie Sie in ETFs investieren und die besten ETFs für Ihr Portfolio finden.</p>
    <div class="publisher-mark">kvm Verlag</div>
  </div>
</div>
</body>
</html>
```